Beauty Salon Industry - Web Design Project

zQuarta is a well-funded start up developing an Online Marketing Platform for small businesses in Europe.
We require a large number of high quality business web designs for our business website builder. Our business websites are seamlessly integrated into our Online Marketing systems and therefore it is important for designers to comply with our Design Guidelines.
This is our second contest and it will focus on the beauty salon industry. We will be running contents every 2-3 weeks for a new industry. Last month, we ran a contest for Builder website designs with 3 top prizes (plus £10 per variation) and we also paid out £25 per design for 20+ entries from designers who did not win the top prizes. So we encourage all entries!
We have included a wire frame this time to encourage you to be as creative as possible with your designs and layout while respecting the following guidelines:
1) You CAN change the layout as much as you like. If you think a vertical menu would look better, then use it. If you think the design would benefit from moving an element to a different location, then you can do that too.
2) You must include ALL the elements in the wire frame in your design.(e.g. latest 2 news entries, a testimonial, 1 gallery image, carousel etc...). Please make sure you have looked through the wire frame and know what is required. Entries that do not include all the elements will not qualify to win.
3) So remember, you CAN change the layout as much as you like but DO NOT remove any elements nor move them to a different page.
4) You may change the size and style of the carousel image. We would like to see as many variations of this as possible.
We are rewarding 3 prizes, and would like the winning designer to design the internal pages to the new design.
As always, if we think your designs could be incorporated into our system, but you do not win the competition, we will reward £25. Therefore, we encourage designers to submit as many designs as possible as we may award up to 25 designs.
Judging criteria : -
1) Visual Design
2) Layout must adhere to best practices and wireframe. If you decide to move elements around significantly please provide reason
3) Functional, informative and drives calls to action
Updates
As usual:
1st place = £350
2nd place = £250
3rd place = £150
Good luck!
Very happy with all the designs submitted so far, and will provide feedback ASAP.
We would like to see you try arranging the elements differently. So please try different navigation types and layouts.
Thanks
Morris
Prize funds for 1st place has been slightly increased.
Thanks
Morris
We have already had some amazing designs submitted. Thanks.
Remember to play with the layout of the elements and try designs with a carousel/slider that is in portrait not just in landscape.
Thanks everyone!
Morris
Hi everyone, we are really enjoying looking through the designs.
We have one NEW requirement. If you have used an image from http://www.frelik-example.com/ in your design, could you please replace it with another.
We are not associated with them.
Thank you.
I have just sent a poll around the office to vote on all the designs and hope to have the results soon.
Good luck and I hope to see all your great designs for our next project in a couple of weeks.
Morris
Hi everyone, we hope you have had a good holiday season. We will be rewarding the prizes very soon, hopefully today or tomorrow.
Thanks
Morris
We are currently going through all the designs that did not win our competition and will be contacting the designers of the designs we would like to use in our system, so please keep an eye on your inbox over the next few days.
Thank you
Morris
Target Market(s)
Beauty Salon Industry
Industry/Entity Type
Beauty Salon
Look and feel
Each slider illustrates characteristics of the customer's brand and the style your logo design should communicate.

```html
<!DOCTYPE html>
<html lang="en">
<head>
<meta charset="utf-8">
<title>Velvet Cut – Hair and Urban Spa</title>
<link href="https://fonts.googleapis.com/css2?family=Noto+Sans:wght@400;700&display=swap" rel="stylesheet">
<style>
:root{
  --green:#6aa82a;
  --green-dark:#4f8d18;
  --btn-top:#8fd33a;
  --btn-bottom:#4f9e14;
  --promo:#7f9a4e;
  --news:#c4f0b0;
  --blue:#1a2fb8;
  --ink:#222;
  --soft:#555;
  --body:#f3f2f3;
  --strip:#dedcdd;
  --footer:#6d6b6d;
  --photo-a:#6f9a4a;
  --photo-b:#d9d6d2;
}
*{margin:0;padding:0;box-sizing:border-box}
html,body{width:1148px;height:1200px;overflow:hidden;background:#fff}
body{position:relative;font-family:"Noto Sans",Verdana,sans-serif;color:var(--ink)}
.abs{position:absolute}
.page{left:36px;top:0;width:1077px;height:1090px;background:#fff;box-shadow:0 0 14px rgba(0,0,0,.25)}
.header-rule{left:36px;top:145px;width:1077px;border-top:1px dashed #aaa}
.body-bg{left:36px;top:146px;width:1077px;height:784px;background:var(--body)}
.brand{left:41px;top:45px;display:flex;align-items:center;gap:14px}
.brand-dot{width:58px;height:58px;border-radius:50%;background:var(--green)}
.brand-name{font-size:46px;font-weight:400;color:var(--green);line-height:1}
.tagline{left:124px;top:96px;font-size:16px;color:#333}
.phone{left:868px;top:40px;display:flex;align-items:center;gap:10px;font-size:16px}
.phone-icon{width:32px;height:32px;border-radius:4px;background:#1f6fb5;display:flex;align-items:center;justify-content:center}
.btn{background:linear-gradient(var(--btn-top),var(--btn-bottom));color:#fff;font-weight:700;border-radius:6px;display:flex;align-items:center;justify-content:center;box-shadow:0 1px 2px rgba(0,0,0,.3)}
.book-now{left:919px;top:75px;width:116px;height:32px;font-size:14px}
.nav{left:56px;top:154px;width:1040px;height:39px;border-radius:8px;background:linear-gradient(#f4f4f4,#dcdcdc);box-shadow:0 2px 2px rgba(0,0,0,.15)}
.nav-item{position:absolute;top:11px;font-size:14.5px;font-weight:700;color:#444;padding-left:14px}
.nav-item::before{content:"";position:absolute;left:0;top:6px;width:6px;height:6px;background:var(--green);transform:rotate(45deg)}
.intro-title{left:77px;top:219px;width:240px;font-size:16.5px;font-weight:700;color:#7bb423;line-height:22px}
.intro-text{width:240px;font-size:12.3px;line-height:20.2px;color:#333;letter-spacing:.3px}
.more{left:263px;top:640px;font-size:14px;font-weight:700;color:var(--green)}
.col-rule{left:341px;top:200px;height:604px;border-left:1px solid #a9cc8a}
.photo{background:linear-gradient(180deg,var(--photo-b) 0%,#c8c5c0 45%,var(--photo-a) 70%,#e4e2df 100%)}
.gallery-photo{left:73px;top:703px;width:220px;height:186px}
.gallery-btn{left:53px;top:898px;width:235px;height:33px;font-size:16px;font-weight:400;justify-content:flex-start;padding-left:26px;border-radius:8px}
.hero{left:362px;top:223px;width:511px;height:327px}
.quote{left:361px;top:571px;width:500px;font-size:14px;line-height:20px}
.quote a,.news a{color:var(--blue);font-weight:700;text-decoration:none}
.quote-author{left:620px;top:618px;width:224px;text-align:right;font-size:14px;font-weight:700}
.quote-link{left:361px;top:645px;width:494px;height:28px;background:#fff;display:flex;align-items:center;padding-left:32px;gap:8px;font-size:12.5px;font-weight:700;color:var(--blue)}
.news{left:345px;top:688px;width:533px;height:216px;background:var(--news)}
.news-rule{left:629px;top:752px;height:152px;border-left:1px solid #9dc88a}
.news-item{position:absolute;top:12px;width:240px}
.news-item h3{font-size:14px;font-weight:700;margin-bottom:16px}
.news-item p{font-size:12.3px;line-height:20.2px}
.news-date{font-size:11.5px;text-align:right;margin-top:12px;letter-spacing:.5px}
.promo{left:883px;top:223px;width:213px;height:214px;background:var(--promo);color:#fff}
.promo-price{position:absolute;left:76px;top:62px;font-size:20px;font-weight:700}
.promo-text{position:absolute;left:31px;top:93px;font-size:14.5px;font-weight:700;line-height:20px}
.promo-btn{left:899px;top:377px;width:188px;height:33px;font-size:13px}
.address-head{left:886px;top:456px;width:204px;height:32px;border:2px solid #8aaa56;background:#fff;color:var(--blue);font-size:16px;font-weight:700;padding:3px 0 0 17px}
.address{left:915px;top:501px;font-size:14px;line-height:20.2px;color:var(--soft)}
.hours-head{left:886px;top:573px;width:201px;height:29px;border-top:1px dashed #8a8fb0;border-bottom:1px dashed #8a8fb0;color:var(--blue);font-size:16px;font-weight:700;padding:3px 0 0 22px}
.hours{left:914px;top:612px;font-size:14px;line-height:20.2px;border-collapse:collapse}
.hours td{padding:0}
.hours td:first-child{width:80px}
.map{left:909px;top:765px;width:164px;height:123px;border-radius:8px;background:linear-gradient(135deg,#d9e6c8,#cfd8d0 55%,#9cc46c)}
.strip{left:36px;top:930px;width:1077px;height:152px;background:var(--strip)}
.thumb{top:953px;width:128px;height:108px}
.footer{left:0;top:1090px;width:1148px;height:110px;background:var(--footer);color:#fff;font-size:16px}
.footer-text{position:absolute;left:758px;top:62px;display:flex;gap:26px}
</style>
</head>
<body>
<div class="abs page"></div>
<div class="abs header-rule"></div>
<div class="abs body-bg"></div>

<div class="abs brand"><span class="brand-dot"></span><span class="brand-name">Velvet Cut</span></div>
<div class="abs tagline">Hair and Urban Spa</div>

<div class="abs phone">
  <span class="phone-icon"><svg width="20" height="20" viewBox="0 0 24 24"><path fill="#fff" d="M6.6 10.8a15.2 15.2 0 0 0 6.6 6.6l2.2-2.2a1 1 0 0 1 1-.25 11.4 11.4 0 0 0 3.6.57 1 1 0 0 1 1 1V20a1 1 0 0 1-1 1A17 17 0 0 1 3 4a1 1 0 0 1 1-1h3.5a1 1 0 0 1 1 1c0 1.25.2 2.45.57 3.57a1 1 0 0 1-.25 1z"/></svg></span>
  <span>020 7946 0834</span>
</div>
<div class="abs btn book-now">Book Now</div>

<nav class="abs nav">
  <span class="nav-item" style="left:101px">Home</span>
  <span class="nav-item" style="left:196px">Services</span>
  <span class="nav-item" style="left:313px">Gallery</span>
  <span class="nav-item" style="left:429px">Testimonials</span>
  <span class="nav-item" style="left:586px">News</span>
  <span class="nav-item" style="left:679px">About Us</span>
  <span class="nav-item" style="left:791px">Contact Us</span>
</nav>

<h1 class="abs intro-title">LET OUR HAIR AND BEAUITY SKILLS BLOW YOU AWAY</h1>
<p class="abs intro-text" style="left:74px;top:283px">Velvet Cut is a passionate creative team,dedicated to delivering a second to none,personal salon experience that will blow your mind.Velvet Cut is a passionate creative team,dedicated to delivering a second to none,personal salon experience that will blow your mind.</p>
<p class="abs intro-text" style="left:69px;top:463px">Velvet Cut is a passionate creative team,dedicated to delivering a second to none,personal salon experience that will blow your mind.Velvet Cut is a passionate creative team,dedicated to delivering a second to none,personal salon experience that will blow your mind.</p>
<div class="abs more">More &gt;</div>
<div class="abs col-rule"></div>

<div class="abs photo gallery-photo" role="img" aria-label="Stacked spa stones on a green woven tray"></div>
<div class="abs btn gallery-btn">Photo Gallery</div>

<div class="abs photo hero" role="img" aria-label="Carousel photo: spa stones and twigs on a green woven tray over white towels"></div>
<p class="abs quote">" MY hairstylist,marisol,was truly amazing.she listed to exactly what i wanted,but also told me exactly what....<a href="#">More</a></p>
<div class="abs quote-author">Elena Varga</div>
<div class="abs quote-link">Quote from the lastest entry on Testmonials page
  <svg width="16" height="16" viewBox="0 0 16 16"><path d="M4 1l8 7-8 7z" fill="var(--green)"/></svg></div>

<section class="abs news">
  <div class="news-item" style="left:14px">
    <h3>Book Now for christmas</h3>
    <p>Our salon is usually very busy for the two weeks before christmas so please book early 020 7946 0300 0r <a href="#">contact us</a></p>
    <div class="news-date" style="margin-right:20px">01 DEC 2011</div>
  </div>
  <div class="news-item" style="left:262px;width:222px">
    <h3 style="margin-bottom:14px">Want to be a hair model?</h3>
    <p>Our salon is usually very busy for the two weeks before christmas so please book early 020 7946 0300 0r <a href="#">contact us</a></p>
    <div class="news-date">01 DEC 2011</div>
  </div>
</section>
<div class="abs news-rule"></div>

<aside class="abs promo">
  <div class="promo-price">£25</div>
  <div class="promo-text">Complimentary gift for<br>first-time clients!</div>
</aside>
<div class="abs btn promo-btn">Book Appointment Now</div>

<div class="abs address-head">Velvet Address</div>
<div class="abs address">12 Hollis Row<br>london<br>W2X 7QT</div>

<div class="abs hours-head">Business Hours</div>
<table class="abs hours">
  <tr><td>Monday</td><td>8.30 - 6</td></tr>
  <tr><td>Tuesday</td><td>8.30 - 6</td></tr>
  <tr><td>Wednesday</td><td>8.30 - 6</td></tr>
  <tr><td>Thursday</td><td>8.30 - 7</td></tr>
  <tr><td>Friday</td><td>8.30 - 6</td></tr>
  <tr><td>Saturday</td><td>8.30 - 6</td></tr>
  <tr><td>Sunday</td><td>10.30 - 5</td></tr>
</table>
<div class="abs map" role="img" aria-label="Street map showing the salon location"></div>

<div class="abs strip"></div>
<div class="abs photo thumb" style="left:80px" role="img" aria-label="Gallery thumbnail of spa stones"></div>
<div class="abs photo thumb" style="left:249px" role="img" aria-label="Gallery thumbnail of spa stones"></div>
<div class="abs photo thumb" style="left:413px" role="img" aria-label="Gallery thumbnail of spa stones"></div>
<div class="abs photo thumb" style="left:591px" role="img" aria-label="Gallery thumbnail of spa stones"></div>
<div class="abs photo thumb" style="left:765px" role="img" aria-label="Gallery thumbnail of spa stones"></div>
<div class="abs photo thumb" style="left:941px" role="img" aria-label="Gallery thumbnail of spa stones"></div>

<footer class="abs footer">
  <div class="footer-text"><span>Managed by zquarta.com</span><span>/</span><span>Admin</span></div>
</footer>
</body>
</html>
```